Business Card Design Project

Build kick ass business card.
Updates

I just uploaded the Vorintex Logo in AI format, for those that were asking. It's looking real good and we'll be reviewing the designs soon. Thanks. 

Target Market(s)

Businesses in many verticals. Focusing on information security.

Vorintex, LLC
Gordon Bexley
Principal Security Consultant
Mobile: +1-602-555-0187
Email: Gordon.Bexley@Vorintex.example
Web: www.vorintex.example

Industry/Entity Type

Business

Requirements
Must have
• Design must look high-end, hi-tech stylish and minimalist

Be different – one that stands out from thousands of others

Does not have to be traditional rectangle

Would like logo integrated

```html
<!DOCTYPE html>
<html lang="en">
<head>
<meta charset="utf-8">
<title>Vorintex Business Card</title>
<link rel="stylesheet" href="https://fonts.googleapis.com/css2?family=Source+Sans+3:wght@400;600;700&display=swap">
<style>
  :root {
    --bg-top: #6b2c76;
    --bg-bottom: #c653c9;
    --card-white: #ffffff;
    --blue-top: #00a9e1;
    --blue-bottom: #0b4e9f;
    --ink: #3b3b3b;
    --ink-soft: #4a4a4a;
    --mark: #2a9fd8;
    --on-blue: #ffffff;
  }
  * { margin: 0; padding: 0; box-sizing: border-box; }
  html, body { width: 1200px; height: 705px; overflow: hidden; }
  body {
    position: relative;
    background: linear-gradient(170deg, var(--bg-top) 0%, #9a3fa3 45%, var(--bg-bottom) 100%);
    font-family: "Source Sans 3", "Myriad Pro", sans-serif;
  }
  .card { position: absolute; overflow: hidden; }
  .card--front { background: var(--card-white); }
  .card--back {
    background: linear-gradient(175deg, var(--blue-top) 0%, #0678c6 45%, var(--blue-bottom) 100%);
    color: var(--on-blue);
    text-align: center;
  }
  .card--large { width: 613px; height: 340px; border-radius: 0 130px 0 150px; }
  .card--small { width: 239px; height: 133px; border-radius: 0 50px 0 58px; }

  .front-large { left: 122px; top: 37px; }
  .back-large { left: 499px; top: 248px; }
  .front-small { left: 37px; top: 544px; }
  .back-small { left: 290px; top: 544px; }

  .brand { position: absolute; }
  .brand__dot { position: absolute; border-radius: 50%; background: var(--mark); }
  .brand__name {
    position: absolute; white-space: nowrap;
    font-weight: 400; color: var(--ink); letter-spacing: 0.02em; line-height: 1;
  }
  .brand__tagline {
    position: absolute; white-space: nowrap;
    color: var(--ink-soft); letter-spacing: 0.12em; line-height: 1;
  }

  .front-large .brand__dot { left: 190px; top: 118px; width: 58px; height: 58px; }
  .front-large .brand__name { left: 280px; top: 126px; font-size: 40px; }
  .front-large .brand__tagline { left: 282px; top: 164px; font-size: 11.5px; }

  .front-small .brand__dot { left: 74px; top: 44px; width: 23px; height: 23px; }
  .front-small .brand__name { left: 109px; top: 47px; font-size: 15.5px; }
  .front-small .brand__tagline { left: 110px; top: 63px; font-size: 4.5px; }

  .person { position: absolute; left: 0; right: 0; }
  .person__name { font-weight: 700; line-height: 1; }
  .person__title { font-weight: 400; line-height: 1; }
  .contact { position: absolute; left: 0; right: 0; list-style: none; }
  .contact li { line-height: 1; }
  .contact__label { margin-right: 0.5em; }

  .back-large .person { top: 116px; }
  .back-large .person__name { font-size: 31px; }
  .back-large .person__title { font-size: 13px; margin-top: 9px; }
  .back-large .contact { top: 230px; font-size: 13.5px; }
  .back-large .contact li + li { margin-top: 4px; }

  .back-small .person { top: 46px; }
  .back-small .person__name { font-size: 12px; }
  .back-small .person__title { font-size: 5px; margin-top: 4px; }
  .back-small .contact { top: 90px; font-size: 5.2px; }
  .back-small .contact li + li { margin-top: 1.6px; }
</style>
</head>
<body>
  <section class="card card--front card--large front-large" aria-label="Card front">
    <div class="brand">
      <span class="brand__dot"></span>
      <span class="brand__name">VORINTEX</span>
      <span class="brand__tagline">network security solutions</span>
    </div>
  </section>

  <section class="card card--back card--large back-large" aria-label="Card back">
    <div class="person">
      <p class="person__name">Gordon Bexley</p>
      <p class="person__title">Principal Security Consultant</p>
    </div>
    <ul class="contact">
      <li><span class="contact__label">Mobile.</span>+1-602-555-0187</li>
      <li><span class="contact__label">Email.</span>Gordon.Bexley@Vorintex.example</li>
      <li><span class="contact__label">Website.</span>www.vorintex.example</li>
    </ul>
  </section>

  <section class="card card--front card--small front-small" aria-label="Card front, actual size">
    <div class="brand">
      <span class="brand__dot"></span>
      <span class="brand__name">VORINTEX</span>
      <span class="brand__tagline">network security solutions</span>
    </div>
  </section>

  <section class="card card--back card--small back-small" aria-label="Card back, actual size">
    <div class="person">
      <p class="person__name">Gordon Bexley</p>
      <p class="person__title">Principal Security Consultant</p>
    </div>
    <ul class="contact">
      <li><span class="contact__label">Mobile.</span>+1-602-555-0187</li>
      <li><span class="contact__label">Email.</span>Gordon.Bexley@Vorintex.example</li>
      <li><span class="contact__label">Website.</span>www.vorintex.example</li>
    </ul>
  </section>
</body>
</html>
```